Brevanor Inc. Website

We need a website design for a new company based in Montreal, Canada. Our company offers professional services in planning & scheduling for major construction projects in varying industries. The main colors to be used are black & red (same as in logo). The final design should convey professionalism, precision, and excellence. The following are examples of what the website layout could look like: https://www.quilvardo.ca/, https://7496.ca/, https://lumavikt.ca/, https://www.dremorhext.com/en. Avoid using stock videos or photos with people in it.
Target audience are multi-national clients looking to hire a firm to manage their construction projects. Target market is Mining & Metals
Mining & Metalurgy, Hydroelectricity, Infrastructure
1 page

```html
<!DOCTYPE html>
<html lang="en">
<head>
<meta charset="utf-8">
<title>Brevanor Inc.</title>
<link href="https://fonts.googleapis.com/css2?family=Russo+One&family=Lato:wght@400;700&display=swap" rel="stylesheet">
<style>
:root{
  --red:#9b0a1c;
  --red-dark:#7f0715;
  --ink:#111111;
  --dark:#231f20;
  --white:#ffffff;
  --grey-text:#6b6b6b;
  --outline:#dcdcdc;
  --field:#ffffff;
}
*{box-sizing:border-box;margin:0;padding:0}
html,body{width:1200px;height:2883px;overflow:hidden;background:var(--white)}
body{font-family:"Lato",sans-serif;color:var(--ink)}
.page{position:relative;width:1200px;height:2883px;overflow:hidden}
.abs{position:absolute}
.display{font-family:"Russo One",sans-serif;text-transform:uppercase}

/* hero */
.hero-photo{left:0;top:0;width:1200px;height:600px;
  background:linear-gradient(180deg,#9fb4cf 0%,#c9b9b4 28%,#d9a574 42%,#8a7b6e 55%,#5b5a60 75%,#3c4048 100%)}
.nav-bar{left:110px;top:0;width:978px;height:77px;background:var(--white);border-radius:0 0 26px 26px;box-shadow:0 4px 10px rgba(0,0,0,.12)}
.brand-disc{left:110px;top:-50px;width:190px;height:190px;border-radius:50%;background:var(--white);display:flex;align-items:center;justify-content:center;padding-top:42px}
.brand-name{font-family:"Lato",sans-serif;font-weight:700;font-size:22px;color:var(--red);letter-spacing:1px}
.nav-links{left:385px;top:28px;display:flex;gap:36px;font-family:"Russo One",sans-serif;font-size:13.5px;text-transform:uppercase;color:#333}
.nav-links .active{color:var(--red);text-decoration:underline}
.btn{display:flex;align-items:center;justify-content:center;border-radius:26px;font-family:"Russo One",sans-serif;text-transform:uppercase;box-shadow:0 4px 8px rgba(0,0,0,.3)}
.nav-cta{left:928px;top:16px;width:144px;height:47px;background:var(--red-dark);color:var(--white);font-size:14px}
.hero-kicker{left:0;width:1200px;top:138px;text-align:center;font-size:27px;color:var(--ink)}
.hero-title{left:0;width:1200px;top:180px;text-align:center;font-size:98px;line-height:1.1;letter-spacing:2px;color:var(--ink)}
.hero-title span{color:var(--red)}
.hero-cta{left:523px;top:294px;width:154px;height:47px;background:var(--ink);color:var(--white);font-size:15px}
.intro-band{left:346px;top:502px;width:854px;height:200px;background:var(--red)}
.intro-text{left:396px;top:542px;width:520px;color:var(--white);font-size:15px;line-height:29px}
.video-disc{left:971px;top:544px;width:116px;height:116px;border-radius:50%;border:3px solid var(--white);background:linear-gradient(135deg,#5b3b30,#b9582e 55%,#3a2a26)}
.video-play{left:1013px;top:586px;width:32px;height:32px;border-radius:50%;background:var(--white);display:flex;align-items:center;justify-content:center}

/* side labels */
.side-label{font-family:"Russo One",sans-serif;text-transform:uppercase;writing-mode:vertical-rl;transform:rotate(180deg);color:transparent;-webkit-text-stroke:1.5px var(--outline);font-size:86px;line-height:1;text-align:center}
.side-services{left:14px;top:752px;height:596px}
.side-about{left:12px;top:1466px;height:380px;-webkit-text-stroke:1.5px rgba(255,255,255,.45);font-size:82px}
.side-contact{left:14px;top:1942px;height:542px}

.section-title{left:0;width:1200px;text-align:center;font-size:41px;color:var(--ink)}
.section-title span{color:var(--red)}
.arc{position:absolute}

/* cards */
.card{width:298px;height:387px;top:903px;background:var(--white);box-shadow:0 3px 12px rgba(0,0,0,.12);border-radius:4px}
.card-photo{position:absolute;left:0;top:0;width:298px;height:233px;border-radius:4px 4px 0 0}
.photo-mining{background:linear-gradient(160deg,#6d7378,#50565a 50%,#8a8478)}
.photo-hydro{background:linear-gradient(170deg,#4fa7c4,#2f8ca8 40%,#5f9a52 70%,#3d7b8a)}
.photo-infra{background:linear-gradient(120deg,#0a1626,#123a6b 45%,#1f8fd4 75%,#0b1a2e)}
.card-label{position:absolute;left:10px;top:197px;width:278px;height:48px;background:var(--white);border-radius:6px 6px 0 0;text-align:center;padding-top:18px;font-size:17px}
.card-body{position:absolute;left:22px;top:245px;width:254px;text-align:center;color:var(--grey-text);font-size:15px;line-height:25px}
.card-link{position:absolute;left:0;width:298px;top:351px;text-align:center;font-size:16px;color:var(--ink);text-decoration:underline}

/* about */
.about-panel{left:0;top:1383px;width:600px;height:551px;background:var(--red)}
.about-photo{left:600px;top:1383px;width:600px;height:551px;background:linear-gradient(180deg,#3e7fc4 0%,#8db7e0 40%,#c9d8e6 65%,#7f8f9d 82%,#2f6f96 100%)}
.about-title{left:113px;top:1452px;font-size:41px;color:var(--white)}
.about-text{left:110px;top:1558px;width:450px;color:var(--white);font-size:15px;line-height:29px}
.about-text p+p{margin-top:29px}
.about-cta{left:111px;top:1809px;width:154px;height:47px;background:var(--white);color:var(--red);font-size:15px}

/* contact */
.address-title{left:129px;top:2094px;font-size:27px}
.info-icon{width:46px;height:46px;border-radius:50%;background:var(--red);display:flex;align-items:center;justify-content:center}
.info-text{font-size:16px;line-height:25px;color:var(--ink)}
.social{width:46px;height:46px;border-radius:50%;background:var(--red)}
.field{background:var(--field);box-shadow:0 2px 8px rgba(0,0,0,.12);font-size:15px;color:#777;padding:16px 17px}
.submit{left:525px;top:2359px;width:142px;height:50px;background:var(--red);color:var(--white);font-size:16px}

/* footer */
.footer{left:0;top:2498px;width:1200px;height:385px;background:var(--dark)}
.footer-brand{left:0;width:1200px;top:2608px;display:flex;align-items:center;justify-content:center;gap:14px}
.footer-brand .dot{width:40px;height:40px;border-radius:50%;background:var(--white)}
.footer-brand .name{font-family:"Lato",sans-serif;font-weight:700;font-size:40px;color:var(--white);letter-spacing:3px}
.footer-nav{left:0;width:1200px;top:2766px;display:flex;justify-content:center;gap:48px;color:var(--white);font-size:16px;font-weight:700}
.copyright{left:0;width:1200px;top:2827px;text-align:center;color:var(--white);font-size:15px}
</style>
</head>
<body>
<div class="page">

  <!-- hero -->
  <div class="abs hero-photo" role="img" aria-label="Aerial view of the Montreal skyline at sunset with the river behind"></div>
  <div class="abs nav-bar"></div>
  <div class="abs brand-disc"><span class="brand-name">BREVANOR</span></div>
  <nav class="abs nav-links">
    <span class="active">Home</span><span>About Us</span><span>Projects</span><span>Gallery</span><span>Latest News</span>
  </nav>
  <div class="abs btn nav-cta">Contact Us</div>

  <div class="abs display hero-kicker">Welcome To</div>
  <h1 class="abs display hero-title">Brev<span>anor</span></h1>
  <div class="abs btn hero-cta">Get Started</div>

  <div class="abs intro-band"></div>
  <p class="abs intro-text">Temporibus autem quibusdam et aut officiis debitis aut rerum necessitatibus saepe udiandae sint et molestiae non recusandae. Itaque earum rerum hic tenetur a sapiente delectus, ut aut reiciendis voluptatibus maiores alias consequatur aut perferendis doloribus asperiores repellat.</p>
  <div class="abs video-disc" role="img" aria-label="Video preview of an industrial site"></div>
  <div class="abs video-play">
    <svg width="14" height="14" viewBox="0 0 14 14"><path d="M3 1 L13 7 L3 13 Z" fill="#9b0a1c"/></svg>
  </div>

  <!-- services -->
  <div class="abs side-label side-services">Services</div>
  <h2 class="abs display section-title" style="top:768px">Our <span>Clients</span></h2>
  <svg class="arc" style="left:528px;top:825px" width="144" height="34" viewBox="0 0 144 34"><path d="M2 32 Q72 -16 142 32" fill="none" stroke="#111" stroke-width="4"/></svg>

  <div class="abs card" style="left:116px">
    <div class="card-photo photo-mining" role="img" aria-label="Open-pit mine with haul trucks"></div>
    <div class="card-label display">Mining &amp; Metallurgy</div>
    <p class="card-body">Temporibus autem quibusdam et aut officiis debitis aut rerum necessitatibus saepe eveniet ut et voluptates repudiandae</p>
    <span class="card-link">READ MORE</span>
  </div>
  <div class="abs card" style="left:454px">
    <div class="card-photo photo-hydro" role="img" aria-label="Aerial view of a hydroelectric dam on a river"></div>
    <div class="card-label display">Hydroelectricity</div>
    <p class="card-body">Itaque earum rerum hic tenetur a sapiente delectus, ut aut reiciendis voluptatibus maiores alias consequatur aut perferendis</p>
    <span class="card-link">READ MORE</span>
  </div>
  <div class="abs card" style="left:791px">
    <div class="card-photo photo-infra" role="img" aria-label="Rows of illuminated server racks"></div>
    <div class="card-label display">Infrastructure</div>
    <p class="card-body">Temporibus autem quibusdam et aut officiis debitis aut rerum necessitatibus saepe eveniet ut et voluptates repudiandae</p>
    <span class="card-link">READ MORE</span>
  </div>

  <!-- about -->
  <div class="abs about-panel"></div>
  <div class="abs about-photo" role="img" aria-label="City skyline with a tall communications tower beside the lake"></div>
  <div class="abs side-label side-about">About</div>
  <h2 class="abs display about-title">About Brevanor</h2>
  <svg class="arc" style="left:114px;top:1506px" width="144" height="34" viewBox="0 0 144 34"><path d="M2 32 Q72 -16 142 32" fill="none" stroke="#fff" stroke-width="4"/></svg>
  <div class="abs about-text">
    <p>Nam libero tempore, cum soluta nobis est eligendi optio cumque at facere possimus, omnis voluptas assumenda est, omnis dolor repellendus. Temporibus autem quibusdam et aut officiis debitis aut rerum &nbsp;molestiae non recusandae.</p>
    <p>Itaque earum rerum hic tenetur a sapiente delectus, ut aut reiciendis voluptatibus maiores alias consequatur aut perferendis doloribus asperiores repellat.</p>
  </div>
  <div class="abs btn about-cta">Read More</div>

  <!-- contact -->
  <div class="abs side-label side-contact">Contact</div>
  <h2 class="abs display section-title" style="top:1986px">Get In <span>Touch With Us</span></h2>
  <svg class="arc" style="left:506px;top:2043px" width="144" height="34" viewBox="0 0 144 34"><path d="M2 32 Q72 -16 142 32" fill="none" stroke="#111" stroke-width="4"/></svg>

  <h3 class="abs display address-title">Address</h3>
  <div class="abs info-icon" style="left:127px;top:2151px">
    <svg width="16" height="20" viewBox="0 0 16 20"><path d="M8 0 C3.6 0 0 3.4 0 7.6 C0 13 8 20 8 20 C8 20 16 13 16 7.6 C16 3.4 12.4 0 8 0 Z" fill="#fff"/><circle cx="8" cy="7.5" r="3" fill="#9b0a1c"/></svg>
  </div>
  <p class="abs info-text" style="left:187px;top:2149px">Brevanor<br>United States</p>
  <div class="abs info-icon" style="left:127px;top:2221px">
    <svg width="18" height="18" viewBox="0 0 24 24"><path d="M6.6 10.8a15.1 15.1 0 0 0 6.6 6.6l2.2-2.2a1 1 0 0 1 1-.25 11.4 11.4 0 0 0 3.6.57 1 1 0 0 1 1 1V20a1 1 0 0 1-1 1A17 17 0 0 1 3 4a1 1 0 0 1 1-1h3.5a1 1 0 0 1 1 1c0 1.25.2 2.45.57 3.57a1 1 0 0 1-.25 1z" fill="#fff"/></svg>
  </div>
  <p class="abs info-text" style="left:184px;top:2232px">+1 514 555 0147</p>
  <div class="abs info-icon" style="left:127px;top:2284px">
    <svg width="18" height="14" viewBox="0 0 18 14"><rect x="0" y="0" width="18" height="14" rx="2" fill="#fff"/><path d="M1 1.5 L9 8 L17 1.5" fill="none" stroke="#9b0a1c" stroke-width="1.6"/></svg>
  </div>
  <p class="abs info-text" style="left:190px;top:2295px">info@brevanor.com</p>

  <div class="abs social" style="left:127px;top:2355px" aria-label="Social profile"></div>
  <div class="abs social" style="left:186px;top:2355px" aria-label="Social profile"></div>
  <div class="abs social" style="left:246px;top:2355px" aria-label="Social profile"></div>
  <div class="abs social" style="left:306px;top:2355px" aria-label="Social profile"></div>

  <div class="abs field" style="left:525px;top:2104px;width:282px;height:49px">First Name</div>
  <div class="abs field" style="left:818px;top:2104px;width:283px;height:49px">Last Name</div>
  <div class="abs field" style="left:525px;top:2166px;width:282px;height:50px">Your Phone</div>
  <div class="abs field" style="left:818px;top:2166px;width:283px;height:50px">Your Email</div>
  <div class="abs field" style="left:525px;top:2230px;width:576px;height:111px">Message</div>
  <div class="abs btn submit">Submit</div>

  <!-- footer -->
  <footer class="abs footer"></footer>
  <div class="abs footer-brand"><span class="dot"></span><span class="name">BREVANOR</span></div>
  <nav class="abs footer-nav">
    <span>HOME</span><span>ABOUT US</span><span>PROJECTS</span><span>GALLERY</span><span>LATEST NEWS</span><span>CONTACT US</span>
  </nav>
  <p class="abs copyright">Copyrights@2023. Brevanor.All Rights Reserved</p>

</div>
</body>
</html>
```